Psychiatric Office Needs a Website- 1st Time Ever!

Been in practice since 2003 with no website, but finally ready to dive in. We are Maplecrest Behavioral Healthcare, a mental health outpatient practice based in Fayetteville, Georgia that sees diverse individuals and families from childhood to advanced age for a variety of conditions. We've grown by word of mouth and referral but would now like to have a digital footprint. Be the pioneer of our website and we will be sure to share. We would like to see designs that are modern, animated, fairly colorful, easy to read, and caters to all ages. Also, we would like the design to take the whole page (not be centered) and can be viewed well on phone/tablet. Please see our outline for more information. Our motto/slogan is: Maplecrest Behavioral Healthcare- A step forward in your wellness journey, so the design should try to reflect that.
Updates

Target Market(s)

Children through elderly

Industry/Entity Type

Medical

Logo Text

Stepping forward in your wellness journey

Number of Pages Required

1 page

Colors

Designer to choose colors to be used in the design.

Requirements
Must have
• Animation or moving pictures.
• Color.
• Concise.
• User friendly
• Diversity in the stock photos

```html
<!DOCTYPE html>
<html lang="en">
<head>
<meta charset="utf-8">
<title>Maplecrest Behavioral Healthcare</title>
<link href="https://fonts.googleapis.com/css2?family=Maven+Pro:wght@400;500;700&family=Roboto:wght@400;500;700&display=swap" rel="stylesheet">
<style>
:root{
  --blue:#2a94d6;
  --blue-dark:#1b7fc1;
  --blue-light:#4fb0ea;
  --green:#6aa834;
  --green-bright:#8cc63f;
  --ink:#222;
  --text:#555;
  --muted:#888;
  --line:#dcdcdc;
  --red:#e0262c;
  --teal:#1f8b9a;
  --dark:#3a3a3a;
  --white:#fff;
}
*{box-sizing:border-box;margin:0;padding:0}
html,body{width:1200px;height:2359px;overflow:hidden;background:var(--white)}
body{position:relative;font-family:'Roboto',Arial,sans-serif;color:var(--text)}
.abs{position:absolute}
.top-rule{left:0;top:0;width:1200px;height:3px;background:var(--green-bright)}
.brand{left:77px;top:40px;display:flex;align-items:center;gap:12px}
.brand-dot{width:44px;height:44px;border-radius:50%;background:var(--blue)}
.brand-name{font-family:'Maven Pro',sans-serif;font-weight:500;font-size:20px;color:var(--blue);line-height:1.15;width:190px}
.call{left:865px;top:38px;display:flex;gap:14px}
.call-label{font-size:13px;color:#444}
.call-number{font-size:23px;font-weight:700;color:#111;margin-top:2px}
.nav{left:77px;top:126px;width:1046px;height:61px;border-radius:9px 9px 0 0;background:linear-gradient(#4db2ee,#1f8ad2);display:flex}
.nav a{height:61px;display:flex;align-items:center;justify-content:center;color:#fff;font-size:15px;text-decoration:none;border-right:1px solid rgba(255,255,255,.25);box-shadow:1px 0 0 rgba(0,0,0,.08)}
.hero{left:77px;top:187px;width:1046px;height:383px;background:linear-gradient(90deg,#3b3b3b 0%,#9a9a9a 35%,#cfcfcf 70%,#e2e2e2 100%)}
.hero-rule{left:77px;top:570px;width:1046px;height:4px;background:var(--green)}
.hero-card{left:795px;top:261px;width:328px;height:164px;background:rgba(40,40,40,.8);padding:26px 22px}
.hero-title{font-family:'Maven Pro',sans-serif;font-weight:700;font-size:24px;line-height:1.2;color:var(--green-bright);text-shadow:1px 1px 2px #000}
.hero-btn{margin-top:16px;width:230px;height:40px;background:linear-gradient(#4db2ee,#1f8ad2);color:#fff;font-size:14px;display:flex;align-items:center;justify-content:center;border-radius:3px}
.dots{left:1028px;top:531px;display:flex;gap:11px}
.dots span{width:10px;height:10px;border-radius:50%;background:#555}
.dots span.on{background:var(--green-bright);box-shadow:0 0 0 2px #fff}
.section-title{width:1200px;left:0;text-align:center;font-family:'Maven Pro',sans-serif;font-weight:400;font-size:36px;color:var(--blue)}
.section-title .g{color:var(--green)}
.about-text{left:175px;top:678px;width:850px;text-align:center;font-size:13.5px;line-height:1.75;color:#555}
.service{top:862px;width:240px}
.service svg{height:88px;display:block}
.service h3{margin-top:14px;height:54px;width:215px;display:flex;align-items:center;font-weight:400;font-size:19.5px;line-height:1.3;color:var(--ink)}
.service .bar{margin-top:10px;width:102px;height:3px;background:var(--green)}
.service p{margin-top:12px;font-size:13.5px;line-height:1.55;color:#666}
.arrow{width:52px;height:52px;border-radius:50%;background:#fff;display:flex;align-items:center;justify-content:center}
.faq-band{left:0;top:1168px;width:1200px;height:414px;background:linear-gradient(90deg,#dfe3e6,#f3f3f3 40%,#ececec 70%,#d9d6d2)}
.faq-box{left:210px;top:1283px;width:794px;background:#fff;border:1px solid var(--line)}
.faq-row{display:flex;border-bottom:1px solid var(--line);height:51px;align-items:center}
.faq-row:last-child{border-bottom:0}
.faq-q{flex:1;padding-left:16px;font-size:15.5px;display:flex;align-items:center;gap:14px}
.faq-q b{color:var(--red);font-size:18px;font-weight:700}
.faq-toggle{width:50px;height:100%;border-left:1px solid var(--line);display:flex;align-items:center;justify-content:center;color:#888;font-size:18px}
.faq-a{padding:10px 20px 10px 40px;border-bottom:1px solid var(--line);font-size:14px;line-height:1.75;color:#444;position:relative;white-space:nowrap}
.faq-more{position:absolute;right:54px;bottom:10px;color:var(--red);text-decoration:underline;font-size:14px;line-height:1.75}
.split-rule{left:0;top:1582px;width:1200px;height:5px;background:#cfcfcf}
.testi-bg{left:0;top:1587px;width:1200px;height:376px;background:#fff}
.bubble{border-radius:50%;background:#f1f1f1}
.testi-card{top:1694px;width:332px;height:181px;background:#fff;border:1px solid var(--line);border-radius:4px;padding:20px 22px}
.testi-card p{font-size:13.5px;line-height:1.55;color:#888}
.testi-card h4{margin-top:8px;font-weight:400;font-size:18px;color:#111}
.testi-card small{display:block;margin-top:4px;font-size:10.5px;font-style:italic;color:#888}
.avatar{width:78px;height:78px;border-radius:50%;background:linear-gradient(#9bb1c4,#6c8aa6);border:4px solid #fff;box-shadow:0 1px 4px rgba(0,0,0,.35)}
.contact-band{left:0;top:1963px;width:1200px;height:345px;background:linear-gradient(90deg,#2e2e2e,#444 50%,#353535)}
.contact-title{color:#fff}
.field{background:#fff;height:40px;font-size:12px;color:#444;padding:12px 12px}
.send{left:461px;top:2180px;width:84px;height:85px;background:linear-gradient(#4db2ee,#1f8ad2);display:flex;align-items:center;justify-content:center}
.divider{left:580px;top:2078px;width:1px;height:188px;background:#777}
.info{left:605px;color:#eee;font-size:14px;line-height:1.6;display:flex;gap:14px}
.info svg{flex:none;margin-top:2px}
.map{left:862px;top:2078px;width:261px;height:187px;background:linear-gradient(135deg,#dfe8cf,#eef0e6 50%,#d5e2c3)}
.footer{left:0;top:2308px;width:1200px;height:51px;background:linear-gradient(#4db2ee,#1f8ad2);color:#fff;font-size:14px;display:flex;align-items:center;justify-content:center}
.footer b{font-weight:700;font-size:15px;margin:0 4px}
</style>
</head>
<body>
<div class="abs top-rule"></div>

<header>
  <div class="abs brand"><span class="brand-dot"></span><span class="brand-name">Maplecrest Behavioral Healthcare</span></div>
  <div class="abs call">
    <svg width="48" height="48" viewBox="0 0 24 24"><path fill="#2a94d6" d="M6.6 10.8a15.1 15.1 0 0 0 6.6 6.6l2.2-2.2c.3-.3.7-.4 1-.2 1.1.4 2.3.6 3.6.6.6 0 1 .4 1 1V20c0 .6-.4 1-1 1C10.6 21 3 13.4 3 4c0-.6.4-1 1-1h3.5c.6 0 1 .4 1 1 0 1.3.2 2.5.6 3.6.1.3 0 .7-.2 1z"/></svg>
    <div><div class="call-label">Call Us Now</div><div class="call-number">555 - 014 - 2290</div></div>
  </div>
  <nav class="abs nav">
    <a style="width:133px">Home</a>
    <a style="width:124px">About</a>
    <a style="width:126px">Services</a>
    <a style="width:228px">Condition We Treat</a>
    <a style="width:177px">New Patients</a>
    <a style="width:174px">Contact Us</a>
    <a style="width:84px;border-right:0;box-shadow:none"><svg width="16" height="16" viewBox="0 0 16 16"><circle cx="6.5" cy="6.5" r="4.8" fill="none" stroke="#fff" stroke-width="2.2"/><path d="M10 10l4.5 4.5" stroke="#fff" stroke-width="2.4"/></svg></a>
  </nav>
</header>

<section>
  <div class="abs hero" role="img" aria-label="Black and white photo of a distressed young woman sitting against a wall"></div>
  <div class="abs hero-rule"></div>
  <div class="abs hero-card">
    <div class="hero-title">A Step Forward In<br>Your Wellness Journey</div>
    <div class="hero-btn">MAKE AN APPOINTMENT</div>
  </div>
  <div class="abs dots"><span class="on"></span><span></span><span></span><span></span></div>
</section>

<section>
  <h2 class="abs section-title" style="top:612px">About <span class="g">Maplecrest Behavioral HealthCare</span></h2>
  <p class="abs about-text">Top level physiotherapy professional, evidenced based treatment. We diagnose the cause and provide you with the best possible treatment. Duas molestias excepturi sint occaecati cupiditate non provident, similique sunt in culpa qui officia deserunt mollitia animi, id est laborum et dolorum fuga.</p>
</section>

<section>
  <h2 class="abs section-title" style="top:792px">Our <span class="g">Services</span></h2>

  <div class="abs arrow" style="left:13px;top:956px;border:2px solid #ccc"><svg width="14" height="14" viewBox="0 0 14 14"><path d="M9 2L4 7l5 5" fill="none" stroke="#999" stroke-width="2"/></svg></div>
  <div class="abs arrow" style="left:1136px;top:956px;border:2px solid var(--blue)"><svg width="14" height="14" viewBox="0 0 14 14"><path d="M5 2l5 5-5 5" fill="none" stroke="#6aa834" stroke-width="2.4"/></svg></div>

  <div class="abs service" style="left:77px">
    <svg width="100" height="88" viewBox="0 0 100 88"><circle cx="50" cy="12" r="9" fill="#2a94d6"/><rect x="2" y="28" width="96" height="10" rx="5" fill="#2a94d6"/><rect x="42" y="26" width="16" height="40" rx="4" fill="#2a94d6"/><circle cx="22" cy="33" r="6" fill="#fff" stroke="#2a94d6" stroke-width="3"/></svg>
    <h3>Diagnostic evaluation and treatment</h3><div class="bar"></div>
    <p>MeetLink end-user training for companies who have purchased MeetLink.</p>
  </div>
  <div class="abs service" style="left:342px">
    <svg width="90" height="88" viewBox="0 0 90 88"><path d="M20 14c8-12 42-12 52 0 14 4 16 26 6 34-4 10-16 12-24 8v26H40V60c-12 4-26 0-30-10C0 40 4 18 20 14z" fill="#2a94d6"/><path d="M28 24c6 4 6 12 0 16M48 18v22M62 28c-4 6 2 12 8 10M36 46c6-2 12 2 14 6" fill="none" stroke="#fff" stroke-width="3" stroke-linecap="round"/></svg>
    <h3>Psychopharmacology</h3><div class="bar"></div>
    <p>Lifecycle Services that include onboarding and adoption services</p>
  </div>
  <div class="abs service" style="left:608px">
    <svg width="88" height="88" viewBox="0 0 88 88"><circle cx="42" cy="44" r="38" fill="none" stroke="#2a94d6" stroke-width="5"/><circle cx="42" cy="44" r="24" fill="#2a94d6"/></svg>
    <h3>Bariatric pre-surgical consultation</h3><div class="bar"></div>
    <p>Migration services, helping existing MeetLink customers migrate their integrated audio solution from one carrier to another.</p>
  </div>
  <div class="abs service" style="left:872px">
    <svg width="60" height="88" viewBox="0 0 60 88"><rect x="4" y="4" width="52" height="76" rx="2" fill="#fff" stroke="#2a94d6" stroke-width="3"/><path d="M12 22h8l4-8 5 14 4-6h15" fill="none" stroke="#2a94d6" stroke-width="3"/><rect x="12" y="40" width="9" height="9" fill="none" stroke="#2a94d6" stroke-width="2"/><path d="M26 44h22M12 58h36M12 68h36" stroke="#2a94d6" stroke-width="3"/></svg>
    <h3>Disability and work-related reports</h3><div class="bar"></div>
    <p>Adoption services to drive the use of MeetLink within an organization.</p>
  </div>
</section>

<section>
  <div class="abs faq-band" role="img" aria-label="Soft faded photo of a counselling session"></div>
  <h2 class="abs section-title" style="top:1216px">Faq's</h2>
  <div class="abs faq-box">
    <div class="faq-row"><div class="faq-q" style="color:var(--teal)"><b>»</b>What are the fees involved, and are there any rebates?</div><div class="faq-toggle">−</div></div>
    <div class="faq-a">Private health rebates should apply if you have 'psychology' as an extra, but we recommend that you<br>call your fund and check your level of cover if this is of concern to you. Unfortunately funds don't give<br>us these details.<span class="faq-more">READ MORE</span></div>
    <div class="faq-row"><div class="faq-q" style="color:var(--red)"><b style="color:var(--teal)">»</b>What happens in a marriage/relationship counselling session?</div><div class="faq-toggle">+</div></div>
    <div class="faq-row"><div class="faq-q" style="color:var(--red)"><b style="color:var(--teal)">»</b>How helpful will it be?</div><div class="faq-toggle">+</div></div>
  </div>
  <div class="abs split-rule"></div>
</section>

<section>
  <div class="abs testi-bg"></div>
  <div class="abs bubble" style="left:80px;top:1600px;width:70px;height:45px"></div>
  <div class="abs bubble" style="left:820px;top:1590px;width:190px;height:140px"></div>
  <div class="abs bubble" style="left:1140px;top:1690px;width:60px;height:40px"></div>
  <div class="abs bubble" style="left:120px;top:1890px;width:40px;height:28px"></div>
  <h2 class="abs section-title" style="top:1626px">Client's <span class="g">Testimonial</span></h2>

  <div class="abs testi-card" style="left:77px"><p>"Lorem Ipsum is simply dummy text of the printing and typesetting industry. Lorem Ipsum has been the industry's standard dummy text ever since the 1500s."</p><h4>Lorem ipsum</h4><small>CEO, Company Name</small></div>
  <div class="abs testi-card" style="left:433px"><p>"Lorem Ipsum is simply dummy text of the printing and typesetting industry. Lorem Ipsum has been the industry's standard dummy text ever since the 1500s."</p><h4>Lorem ipsum</h4><small>CEO, Company Name</small></div>
  <div class="abs testi-card" style="left:789px"><p>"Lorem Ipsum is simply dummy text of the printing and typesetting industry. Lorem Ipsum has been the industry's standard dummy text ever since the 1500s."</p><h4>Lorem ipsum</h4><small>CEO, Company Name</small></div>
  <div class="abs avatar" style="left:286px;top:1836px" role="img" aria-label="Client portrait photo"></div>
  <div class="abs avatar" style="left:642px;top:1836px" role="img" aria-label="Client portrait photo"></div>
  <div class="abs avatar" style="left:998px;top:1836px" role="img" aria-label="Client portrait photo"></div>
</section>

<section>
  <div class="abs contact-band" role="img" aria-label="Dark tinted photo of a group of people"></div>
  <h2 class="abs section-title contact-title" style="top:2010px">Contact Us</h2>
  <div class="abs field" style="left:77px;top:2078px;width:229px">Name</div>
  <div class="abs field" style="left:316px;top:2078px;width:229px">Phone</div>
  <div class="abs field" style="left:77px;top:2128px;width:468px">E-Mail</div>
  <div class="abs field" style="left:77px;top:2180px;width:375px;height:85px">Message</div>
  <div class="abs send"><svg width="36" height="26" viewBox="0 0 36 26"><rect x="1" y="1" width="34" height="24" fill="none" stroke="#fff" stroke-width="2"/><path d="M1 1l17 13L35 1M1 25l12-12M35 25L23 13" fill="none" stroke="#fff" stroke-width="2"/></svg></div>
  <div class="abs divider"></div>
  <div class="abs info" style="top:2108px"><svg width="20" height="26" viewBox="0 0 20 26"><path d="M10 1a8 8 0 0 0-8 8c0 6 8 15 8 15s8-9 8-15a8 8 0 0 0-8-8z" fill="none" stroke="#eee" stroke-width="1.6"/><circle cx="10" cy="9" r="3" fill="none" stroke="#eee" stroke-width="1.6"/></svg><span>123 Building Name, Street<br>Name, City, Country - Zipcode</span></div>
  <div class="abs info" style="top:2173px"><svg width="20" height="20" viewBox="0 0 24 24"><path fill="none" stroke="#eee" stroke-width="1.6" d="M6.6 10.8a15 15 0 0 0 6.6 6.6l2.2-2.2c.3-.3.7-.4 1-.2 1.1.4 2.3.6 3.6.6.6 0 1 .4 1 1V20c0 .6-.4 1-1 1C10.6 21 3 13.4 3 4c0-.6.4-1 1-1h3.5c.6 0 1 .4 1 1 0 1.3.2 2.5.6 3.6.1.3 0 .7-.2 1z"/></svg><span>555 014 2290</span></div>
  <div class="abs info" style="top:2213px"><svg width="20" height="16" viewBox="0 0 20 16"><rect x="1" y="1" width="18" height="14" rx="1" fill="none" stroke="#eee" stroke-width="1.6"/><path d="M1 2l9 7 9-7" fill="none" stroke="#eee" stroke-width="1.6"/></svg><span>info@maplecresthealthcare.com</span></div>
  <div class="abs map" role="img" aria-label="Location map of the practice"></div>
</section>

<footer class="abs footer">© <b>Maplecrest Behavioral Healthcare</b> - 2017. All Rights Reserved</footer>
</body>
</html>
```